Clipvane video - Halvern Quobo piano instrumental music

Hi,
A couple of years ago I produced a Halvern Quobo piano instrumental album

I'm looking for a video to post on clipvane that will feature all my songs from this album. The album is popular for sleeping / study / calming / peaceful / background music. So the video to have some sort of these elements.

The music goes for 1hour 1 minute and their are 20 tracks.

I was thinking with the video to display the song title and movie title could be displayed with each track as it plays in the background. Preferably no copyrighted video from halvern/quobo that would infringe on copyright.

Requirements
Must have
• Music in background here are the original tracks.
• https://www.filecrate-example.net/sh/k3rq8tz0pwlxmne/BBxnTqL-PzoR-_QW7hjFnRkdwe?dl=0
• I'm looking for a video to be produced (e.g. animation or a still that will roll through the song titles as the music is played)
• Tunelark Official Release
• https://listen.tunelark-example.net/album/8Kqwzr3vbHn27D4mUtRaxp
Nice to have
• Other social media links (either start or end of video where it would fit best)
• Snapmere link: snapmere-example.net/tobyhallowaymusic
• Friendloop Fan Page: friendloop-example.net/tobyhallowaypianist
• Wavehollow: wavehollow-example.net/tobyhallowaypianist
• Website: tobyhalloway-example.com.au
• Tunelark: https://listen.tunelark-example.net/artist/9dRZ47QwPLmGVcX2b81kzq?si=Tx3PbnwqEzFr7GkaYHp29v
• Pearfruit Audio: https://audio.pearfruit-example.net/au/artist/toby-halloway/4830192746
Should not have
• Copyrighted material from halvern and quobo films

```html
<!DOCTYPE html>
<html lang="en">
<head>
<meta charset="UTF-8">
<title>Relax – Toby Halloway</title>
<link rel="stylesheet" href="https://fonts.googleapis.com/css2?family=Inter:wght@400;500;700;800&display=swap">
<style>
  :root {
    --ink-white: #ffffff;
    --accent-aqua: #64e8dc;
    --photo-dark: #1f1f1f;
    --photo-mid: #474747;
    --photo-light: #8a8a8a;
    --veil: rgba(20, 20, 20, 0.35);
  }
  html, body {
    margin: 0;
    padding: 0;
    width: 1200px;
    height: 675px;
    overflow: hidden;
    background: #000;
  }
  .cover {
    position: relative;
    width: 1200px;
    height: 675px;
    overflow: hidden;
    font-family: "Inter", "Helvetica Neue", Arial, sans-serif;
    color: var(--ink-white);
  }
  .cover__photo {
    position: absolute;
    inset: 0;
    background:
      radial-gradient(ellipse 55% 45% at 40% 30%, rgba(0,0,0,0.55), transparent 70%),
      radial-gradient(ellipse 60% 50% at 85% 85%, var(--photo-light), transparent 75%),
      radial-gradient(ellipse 40% 35% at 10% 75%, #6f6f6f, transparent 70%),
      linear-gradient(160deg, var(--photo-dark) 0%, var(--photo-mid) 55%, #5e5e5e 100%);
  }
  .cover__veil {
    position: absolute;
    inset: 0;
    background: var(--veil);
  }
  .cover__title {
    position: absolute;
    left: 0;
    right: 0;
    top: 272px;
    margin: 0;
    text-align: center;
    font-weight: 700;
    font-size: 124px;
    line-height: 1;
    letter-spacing: 0.13em;
    padding-left: 0.13em;
    color: var(--accent-aqua);
  }
  .brand {
    position: absolute;
    left: 67px;
    top: 571px;
    display: flex;
    align-items: center;
    gap: 9px;
  }
  .brand__mark {
    width: 50px;
    height: 50px;
    border: 2px solid var(--ink-white);
    border-radius: 50%;
    box-sizing: border-box;
  }
  .brand__name {
    font-size: 16px;
    font-weight: 500;
    letter-spacing: 0.02em;
    text-transform: uppercase;
  }
  .links {
    position: absolute;
    top: 562px;
    text-align: center;
  }
  .links__label {
    margin: 0 0 14px;
    font-size: 12px;
    font-weight: 500;
    letter-spacing: 0.14em;
    text-transform: uppercase;
  }
  .links__list {
    display: flex;
    justify-content: center;
    gap: 18px;
    font-size: 17px;
    font-weight: 700;
  }
  .links--social { left: 720px; width: 140px; }
  .links--social .links__list { font-size: 14px; gap: 12px; }
  .links--stream { left: 915px; width: 235px; top: 558px; }
  .links--stream .links__list { font-size: 18px; }
</style>
</head>
<body>
  <main class="cover">
    <div class="cover__photo" role="img" aria-label="Black and white photo of a woman peacefully asleep in white bed sheets"></div>
    <div class="cover__veil"></div>

    <h1 class="cover__title">RELAX</h1>

    <div class="brand">
      <span class="brand__mark"></span>
      <span class="brand__name">Toby Halloway</span>
    </div>

    <div class="links links--social">
      <p class="links__label">Follow me</p>
      <div class="links__list">
        <span>Friendloop</span>
        <span>Snapmere</span>
      </div>
    </div>

    <div class="links links--stream">
      <p class="links__label">Available on</p>
      <div class="links__list">
        <span>Tunelark</span>
        <span>Pearfruit Audio</span>
      </div>
    </div>
  </main>
</body>
</html>
```